Personal Trainer. Ruvane PT. Needs poster to attract clients.

I need a poster to attract clients to my business Ruvane PT.
The demographic I am targeting is 30-45 year old overweight women and men. I would like some gym pictures incorporated. (these should not be pics of athletes/super fit body types)These are up to you. Please note my target market as super fit models would not be appropriate.
I am fond of the black background but I am open to change.

I wanted my contact details to be
Phone number- 0427 380 615
and
Facebook- Ruvane PT.
No email, website or street address please
I would like a small picture of myself near the contact details but do not want my photo to be a feature.

Attached is my old poster design.
****PLEASE NOTE CHANGES ABOVE****

Target Market(s)

Both overweight women and men 30-45 years old

Industry/Entity Type

Business

Requirements
Should not have
• Street address
• Web address
• Pics of super fit athletes

```html
<!DOCTYPE html>
<html lang="en">
<head>
<meta charset="utf-8">
<title>Ruvane PT – Personal Trainer Poster</title>
<link rel="stylesheet" href="https://fonts.googleapis.com/css2?family=Lato:wght@300;400;700;900&family=Archivo+Black&display=swap">
<style>
  :root {
    --ink: #07070a;
    --yellow: #f7d117;
    --gold: #f2a20c;
    --blue: #1485cf;
    --silver-light: #ececef;
    --silver-dark: #6e6e74;
    --white: #ffffff;
    --gym-light: #8a7260;
    --gym-mid: #5a4738;
    --gym-dark: #241c17;
    --skin-warm: #9a5f3e;
    --skin-deep: #4a2a1a;
    --portrait-skin: #d79a82;
    --portrait-shirt: #1a1a1d;
  }
  * { margin: 0; padding: 0; box-sizing: border-box; }
  html, body { width: 849px; height: 1200px; overflow: hidden; background: var(--ink); }
  .poster {
    position: relative;
    width: 849px;
    height: 1200px;
    overflow: hidden;
    background: var(--ink);
    font-family: "Lato", Arial, sans-serif;
    color: var(--white);
  }
  .hero-photo {
    position: absolute;
    left: 0; top: 0;
    width: 849px; height: 640px;
    background:
      radial-gradient(ellipse 300px 340px at 600px 200px, #a68a72 0%, rgba(166,138,114,0) 75%),
      radial-gradient(ellipse 120px 200px at 320px 320px, #8c6a55 0%, rgba(140,106,85,0) 80%),
      linear-gradient(180deg, var(--gym-dark) 0%, var(--gym-mid) 45%, var(--gym-light) 80%, var(--gym-mid) 100%);
  }
  .arc-band {
    position: absolute;
    left: 0; top: 360px;
    width: 849px; height: 840px;
  }
  .feature-photo {
    position: absolute;
    left: 640px; top: 640px;
    width: 209px; height: 560px;
    border-radius: 120px 0 0 0;
    background:
      radial-gradient(ellipse 140px 240px at 140px 330px, var(--skin-warm) 0%, var(--skin-deep) 65%, rgba(74,42,26,0.6) 100%),
      var(--skin-deep);
  }
  .trainer-photo {
    position: absolute;
    left: 0; top: 956px;
    width: 206px; height: 244px;
    border-radius: 0 16px 0 0;
    background:
      radial-gradient(ellipse 52px 64px at 88px 72px, var(--portrait-skin) 0%, #b0725c 70%, rgba(176,114,92,0) 100%),
      linear-gradient(180deg, #3a3a3f 0%, #2a2a2e 50%, var(--portrait-shirt) 52%, var(--portrait-shirt) 100%);
  }
  .brand {
    position: absolute;
    left: 0; top: 462px;
    width: 849px;
    text-align: center;
    font-family: "Archivo Black", "Arial Black", sans-serif;
    font-size: 52px;
    letter-spacing: 3px;
    color: var(--yellow);
    line-height: 1;
  }
  .headline {
    position: absolute;
    left: 0;
    width: 849px;
    text-align: center;
    font-weight: 900;
    line-height: 1;
    white-space: nowrap;
  }
  .role {
    top: 578px;
    font-size: 76px;
    letter-spacing: -1px;
    background: linear-gradient(90deg, var(--silver-dark) 0%, var(--silver-light) 30%, #9a9aa0 55%, var(--silver-light) 80%, var(--silver-dark) 100%);
    -webkit-background-clip: text;
    background-clip: text;
    color: transparent;
  }
  .trainer-name {
    top: 660px;
    font-weight: 700;
    font-size: 106px;
    letter-spacing: -2px;
    background: linear-gradient(180deg, var(--yellow) 0%, var(--yellow) 45%, var(--gold) 100%);
    -webkit-background-clip: text;
    background-clip: text;
    color: transparent;
  }
  .tagline {
    position: absolute;
    left: 176px; top: 816px;
    line-height: 1;
    white-space: nowrap;
  }
  .tagline-light { display: block; font-weight: 300; font-size: 77px; letter-spacing: 1px; }
  .tagline-bold { display: block; font-weight: 900; font-size: 74px; margin-top: 0; }
  .contact {
    position: absolute;
    left: 268px; top: 1118px;
  }
  .contact-row { display: flex; align-items: center; height: 30px; }
  .contact-row + .contact-row { margin-top: 8px; }
  .call-pill {
    display: inline-block;
    width: 124px; height: 24px;
    border-radius: 12px;
    background: linear-gradient(180deg, #7cc4ef 0%, var(--blue) 55%, #0d62a0 100%);
    font-weight: 900;
    font-size: 17px;
    line-height: 24px;
    text-align: center;
    letter-spacing: 0.5px;
    color: var(--white);
  }
  .phone { margin-left: 9px; font-weight: 900; font-size: 28px; }
  .social-mark {
    display: inline-block;
    width: 25px; height: 25px;
    background: var(--blue);
    border-radius: 3px;
  }
  .social-name { margin-left: 8px; font-weight: 400; font-size: 26px; }
</style>
</head>
<body>
<main class="poster">
  <div class="hero-photo" role="img" aria-label="Gym photo: a trainer coaching a client performing a barbell front squat in a dim warehouse gym"></div>

  <svg class="arc-band" viewBox="0 0 849 840" aria-hidden="true">
    <path d="M0 200 Q 250 5 560 8 L 570 840 L 0 840 Z" fill="var(--yellow)"/>
    <path d="M560 8 Q 760 12 849 230 L 849 840 L 560 840 Z" fill="var(--blue)"/>
    <path d="M0 238 Q 300 22 560 28 Q 760 36 849 280 L 849 840 L 0 840 Z" fill="var(--ink)"/>
  </svg>

  <div class="feature-photo" role="img" aria-label="Gym photo: a person training with a dumbbell"></div>
  <div class="trainer-photo" role="img" aria-label="Small portrait of the personal trainer in a branded polo shirt"></div>

  <div class="brand">RUVANE PT</div>

  <h1 class="headline role">PERSONAL TRAINER</h1>
  <h2 class="headline trainer-name">DALE MARSTON</h2>

  <p class="tagline">
    <span class="tagline-light">BUILDING A</span>
    <span class="tagline-bold">BETTER YOU</span>
  </p>

  <div class="contact">
    <div class="contact-row">
      <span class="call-pill">CALL NOW</span>
      <span class="phone">0427 380 615</span>
    </div>
    <div class="contact-row">
      <span class="social-mark"></span>
      <span class="social-name">Ruvane PT.</span>
    </div>
  </div>
</main>
</body>
</html>
```